Seeds of Renewal needs a business card design

I need a business card design for my company to promote my new Christian non-fiction book, "Where the Quiet River Bends." I also want it to promote my web site, www.seedsofrenewalway.com. The book is about empowering people to be transformed through a deeper relationship with God. I am picturing a design with a dove over water that matches the colors of my book cover, blue, white, yellow, and orange. Fire and light would also be possible elements of the design. I would like to be able to use the dove by itself as a logo for my business. This is my first book and I do not know if others will follow. The name of my publishing company is Lantern Valley Press, named after Gideon in the Bible story from the book of Judges. My book was independently published and was recently selected as a finalist for the 2015 Bright Horizon SMALLPRESS book prize in the Christian non-fiction genre.

Target Market(s)

People who are hungry for more of God and who want to experience deep change in their lives.

Industry/Entity Type

Business

Contact Information for Business Card

Dana Whitfield
Author
Where the Quiet River Bends
4283 Maple Hollow Lane
Austin, Texas 78952-1184
512-555-0147 512-555-0193
dana-whitfield@brightmailbox.net
www.seedsofrenewalway.com

Colors
0355a3
3377b5
85acd3
cedeed
fbee3e
ffc214

Requirements
Must have
• A dove with a blue background, peaceful and appealing
Nice to have
• Water and fire or light
Should not have
• Violence or fear-producing images

```html
<!DOCTYPE html>
<html lang="en">
<head>
<meta charset="utf-8">
<title>Dana Whitfield – Business Card</title>
<link rel="stylesheet" href="https://fonts.googleapis.com/css2?family=Dancing+Script:wght@500;700&display=swap">
<style>
  :root {
    --stage: #2b2b2b;
    --royal: #0355a3;
    --sky: #3377b5;
    --mist: #85acd3;
    --pale: #cedeed;
    --gold: #fbee3e;
    --white: #ffffff;
    --deep: #023b78;
  }
  * { box-sizing: border-box; margin: 0; padding: 0; }
  html, body {
    width: 1200px;
    height: 846px;
    overflow: hidden;
    background: var(--stage);
  }
  .business-card {
    position: absolute;
    left: 100px;
    top: 137px;
    width: 1000px;
    height: 572px;
    overflow: hidden;
    background: linear-gradient(160deg, var(--sky) 0%, var(--royal) 50%, var(--deep) 100%);
    font-family: "Dancing Script", cursive;
  }
  .moon-disc {
    position: absolute;
    left: 0;
    top: 0;
    width: 1000px;
    height: 572px;
  }
  .dove-artwork {
    position: absolute;
    left: 70px;
    top: 30px;
    width: 380px;
    height: 150px;
    border-radius: 50%;
    background: radial-gradient(ellipse at 40% 50%, var(--white) 0%, var(--pale) 40%, rgba(206,222,237,0) 72%);
  }
  .water-splash {
    position: absolute;
    left: 0;
    top: 180px;
    width: 330px;
    height: 250px;
    border-radius: 50%;
    background: radial-gradient(ellipse at 50% 50%, rgba(206,222,237,0.8) 0%, rgba(133,172,211,0.45) 45%, rgba(133,172,211,0) 72%);
  }
  .contact-block {
    position: absolute;
    right: 48px;
    top: 160px;
    width: 600px;
    text-align: right;
    color: var(--gold);
    font-weight: 500;
    font-size: 27px;
    line-height: 1.3;
  }
  .author-name {
    color: var(--white);
    font-weight: 700;
    font-size: 52px;
    line-height: 1.1;
    margin-bottom: 6px;
  }
  .contact-group { margin-top: 16px; }
</style>
</head>
<body>
  <main class="business-card">
    <svg class="moon-disc" viewBox="0 0 1000 572" aria-hidden="true">
      <circle cx="250" cy="130" r="300" fill="#3377b5" fill-opacity="0.45" stroke="#85acd3" stroke-opacity="0.5" stroke-width="2"/>
    </svg>
    <div class="dove-artwork" role="img" aria-label="White dove in flight with wings spread"></div>
    <div class="water-splash" role="img" aria-label="Sparkling splash of water rising below the dove"></div>
    <section class="contact-block">
      <h1 class="author-name">Dana Whitfield</h1>
      <p class="author-title">Author: Where the Quiet River Bends</p>
      <p class="address-line">Address: 4283 Maple Hollow Lane</p>
      <p class="address-line">Austin, Texas 78952-1184</p>
      <div class="contact-group">
        <p class="phone-line">Tel: 512-555-0147 512-555-0193</p>
        <p class="email-line">Email: dana-whitfield@brightmailbox.net</p>
        <p class="website-line">Website: www.seedsofrenewalway.com</p>
      </div>
    </section>
  </main>
</body>
</html>
```